Business Card Design

I need a business card design for a photography business that specializes in headshots and portraits.

Target Market(s)

Business professionals, actors, actresses

Industry/Entity Type

Business

Contact Information for Business Card

Cobalt Ridge Photography, Greg Whitlow, 5817 Kellerman Ave, Suite 416, Fort Wayne, IN 46915, 260.555.0187, www.cobaltridgephoto.example. greg.whitlow@cobaltridgephoto.example

Requirements
Must have
• The business card should state the type of photography services offered: headshots and portraits.

```html
<!DOCTYPE html>
<html lang="en">
<head>
<meta charset="utf-8">
<title>Cobalt Ridge Photography – Business Card</title>
<link href="https://fonts.googleapis.com/css2?family=Didact+Gothic&display=swap" rel="stylesheet">
<style>
  :root {
    --backdrop: #9fd8ef;
    --card: #ffffff;
    --teal: #1f9a9c;
    --ink: #222222;
    --muted: #8a8a8a;
    --portrait-dark: #1a1a1a;
    --portrait-light: #b5b5b5;
  }
  * { margin: 0; padding: 0; box-sizing: border-box; }
  html, body {
    width: 1200px;
    height: 873px;
    overflow: hidden;
    background: var(--backdrop);
    font-family: "Didact Gothic", "Century Gothic", sans-serif;
  }
  .business-card {
    position: absolute;
    left: 250px;
    top: 236px;
    width: 700px;
    height: 400px;
    background: var(--card);
    overflow: hidden;
    box-shadow: 0 14px 40px rgba(20, 80, 110, 0.25);
  }
  .portrait-area {
    position: absolute;
    left: 0;
    top: 96px;
    width: 290px;
    height: 230px;
    background: linear-gradient(135deg, var(--portrait-dark) 0%, #4a4a4a 45%, var(--portrait-light) 100%);
  }
  .studio-name {
    position: absolute;
    right: 30px;
    top: 20px;
    font-size: 44px;
    font-weight: 400;
    line-height: 1.2;
    color: var(--teal);
    white-space: nowrap;
  }
  .photographer-name {
    position: absolute;
    right: 150px;
    top: 104px;
    font-size: 26px;
    color: var(--ink);
    white-space: nowrap;
  }
  .services {
    position: absolute;
    right: 138px;
    top: 142px;
    font-size: 14px;
    color: var(--ink);
    white-space: nowrap;
  }
  .contact-panel {
    position: absolute;
    right: 0;
    bottom: 0;
    width: 420px;
    height: 190px;
  }
  .contact-panel svg { position: absolute; inset: 0; }
  .contact-details {
    position: absolute;
    right: 24px;
    top: 62px;
    color: #ffffff;
    font-size: 14px;
    font-style: normal;
    line-height: 1.65;
    text-align: right;
    white-space: nowrap;
  }
  .website {
    position: absolute;
    left: 26px;
    bottom: 30px;
    font-size: 13px;
    letter-spacing: 1.5px;
    text-transform: uppercase;
    color: var(--muted);
    white-space: nowrap;
  }
</style>
</head>
<body>
  <main class="business-card">
    <div class="portrait-area" role="img" aria-label="Illustration of a woman with long dark curly hair"></div>

    <h1 class="studio-name">Cobalt Ridge Photography</h1>
    <p class="photographer-name">Greg Whitlow</p>
    <p class="services">specializing in headshots and portraits</p>

    <section class="contact-panel">
      <svg width="420" height="190" viewBox="0 0 420 190" aria-hidden="true">
        <path d="M40 190 C40 80 130 0 240 0 L420 0 L420 190 Z" fill="var(--teal)"/>
      </svg>
      <address class="contact-details">
        5817 Kellerman Ave, Suite 416<br>
        Fort Wayne, IN 46915<br>
        260.555.0187<br>
        greg.whitlow@cobaltridgephoto.example
      </address>
    </section>

    <p class="website">www.cobaltridgephoto.example</p>
  </main>
</body>
</html>
```